依頼詳細
制作条件は下記の通り。
1)スマホのトップページのデザイン。ただしトップページ全体の制作は不要で、原則は最初に表示される画面のみでよい。ただしデザインをよりわかりやすくするために、最初に表示される画面に加えてその下部の若干のデザインを含むのは自由。
2)ロゴは添付のデータを用いる。
3)指定色のレッドをブランドカラーとして強調し、サイト名の中にある「+」を象徴的に使うことが望ましい。
4)既存マッチングサイトとは一線を画する、斬新なイメージであること。
5)都会的で洗練されたデザインであるとともに、見た目の美しさだけのレベルにとどまらず、「おー!」と見た人を驚かせるようなインパクトのあるデザインであること。
6)モデル撮影やレンタルフォトの使用なども可能。その場合はダミーのイメージを置いておく。
7)キャッチコピーがあったほうがよい場合はダミーのコピーを置いておく。
8)デザインは添付の「スマホ画面」の画面にレイアウトして、JPEGデータで提出。
ページ数
1ページ
希望イメージ
シンプル 複雑
単色 カラフル
暗い 明るい
日常 高級
遊び心 厳粛
未来的 伝統的
女性的 男性的
希望する色
赤系
補足説明
最終納品はイラストレーター形式ですが、応募はJPEGにてお願いします。
添付の「スマホ画面」の画面にレイアウトしてください。
たくさんの応募をいただきましたが、従来のマッチングサイトとは異なる「斬新」「サプライズ」という点で該当するものがあまりありませんでした。
つきましては、期間延長をさせていだきますので、この点をご理解をいただき私たちを「あっ!」っと言わせるような作品を応募いただけることを願っております。
■ 選んだ理由

シンプルで操作性に秀でた作品だと感じました。

■ 提案者全員のお礼・コメント

みなさま、
たくさんの素敵な作品をありがとうございました!

```html
<!DOCTYPE html>
<html lang="ja">
<head>
<meta charset="utf-8">
<title>Enmusubi トップ画面</title>
<link rel="stylesheet" href="https://fonts.googleapis.com/css2?family=Montserrat:wght@600&display=swap">
<style>
  :root {
    --brand-red: #c1262c;
    --tile-white: #ffffff;
    --icon-red: #c1262c;
    --text-white: #ffffff;
  }
  * { box-sizing: border-box; margin: 0; padding: 0; }
  html, body {
    width: 1200px;
    height: 2208px;
    overflow: hidden;
    background: var(--brand-red);
  }
  .screen {
    position: relative;
    width: 1200px;
    height: 2208px;
    background: var(--brand-red);
  }
  .brand {
    position: absolute;
    top: 170px;
    left: 0;
    width: 100%;
    text-align: center;
  }
  .brand-name {
    font-family: "Montserrat", sans-serif;
    font-weight: 600;
    font-size: 64px;
    letter-spacing: 1px;
    color: var(--text-white);
  }
  .menu-grid {
    position: absolute;
    top: 430px;
    left: 60px;
    width: 1080px;
    height: 1500px;
    display: grid;
    grid-template-columns: repeat(3, 1fr);
    grid-template-rows: repeat(4, 1fr);
    gap: 16px;
    list-style: none;
  }
  .menu-tile {
    background: var(--tile-white);
    display: flex;
    align-items: center;
    justify-content: center;
  }
  .menu-icon {
    width: 210px;
    height: 210px;
    fill: var(--icon-red);
    stroke: none;
  }
  .menu-icon .line { fill: none; stroke: var(--icon-red); stroke-width: 7; stroke-linecap: round; stroke-linejoin: round; }
  .menu-icon .cut { fill: var(--tile-white); }
</style>
</head>
<body>
<main class="screen">
  <header class="brand">
    <span class="brand-name">Enmusubi</span>
  </header>

  <ul class="menu-grid">
    <!-- location -->
    <li class="menu-tile" aria-label="エリア検索">
      <svg class="menu-icon" viewBox="0 0 100 100">
        <path d="M50 10a27 27 0 0 1 27 27c0 22-27 50-27 50S23 59 23 37A27 27 0 0 1 50 10z"/>
        <circle class="cut" cx="50" cy="37" r="10"/>
        <path class="line" d="M34 92h32"/>
      </svg>
    </li>
    <!-- globe -->
    <li class="menu-tile" aria-label="ワールド">
      <svg class="menu-icon" viewBox="0 0 100 100">
        <circle cx="50" cy="50" r="38"/>
        <g class="line" style="stroke:var(--tile-white);stroke-width:4">
          <ellipse cx="50" cy="50" rx="16" ry="38"/>
          <path d="M50 12v76M14 38h72M14 62h72"/>
        </g>
      </svg>
    </li>
    <!-- up / down -->
    <li class="menu-tile" aria-label="並び替え">
      <svg class="menu-icon" viewBox="0 0 100 100">
        <path d="M34 12l20 26H42v50H26V38H14z"/>
        <path d="M66 88L46 62h12V12h16v50h12z"/>
      </svg>
    </li>
    <!-- refresh cycle -->
    <li class="menu-tile" aria-label="更新">
      <svg class="menu-icon" viewBox="0 0 100 100">
        <g class="line" style="stroke-width:11;stroke-linecap:butt">
          <path d="M30 28A32 32 0 0 1 72 26"/>
          <path d="M82 50A32 32 0 0 1 62 80"/>
          <path d="M36 82A32 32 0 0 1 18 48"/>
        </g>
        <path d="M68 14l14 18-22 4z"/>
        <path d="M70 92l-24-4 14-16z"/>
        <path d="M8 42l18-14 4 22z"/>
      </svg>
    </li>
    <!-- gas cylinder -->
    <li class="menu-tile" aria-label="サービス">
      <svg class="menu-icon" viewBox="0 0 100 100">
        <rect x="28" y="30" width="44" height="62" rx="10"/>
        <rect x="42" y="16" width="16" height="14"/>
        <path class="line" d="M50 16V8h14v10M36 46h28"/>
      </svg>
    </li>
    <!-- map search -->
    <li class="menu-tile" aria-label="マップ検索">
      <svg class="menu-icon" viewBox="0 0 100 100">
        <path d="M8 22l28-8 28 8 28-8v64l-28 8-28-8-28 8z"/>
        <path class="line" style="stroke:var(--tile-white);stroke-width:4" d="M36 14v64M64 22v64"/>
        <circle class="cut" cx="60" cy="54" r="17"/>
        <circle class="line" cx="60" cy="54" r="10"/>
        <path class="line" style="stroke-width:9" d="M68 62l14 14"/>
      </svg>
    </li>
    <!-- cocktail -->
    <li class="menu-tile" aria-label="グルメ">
      <svg class="menu-icon" viewBox="0 0 100 100">
        <path d="M18 36h64c0 20-14 32-32 32S18 56 18 36z"/>
        <path class="line" d="M50 68v20M34 90h32M54 36l20-28"/>
        <circle cx="34" cy="28" r="10"/>
      </svg>
    </li>
    <!-- sunflower -->
    <li class="menu-tile" aria-label="アウトドア">
      <svg class="menu-icon" viewBox="0 0 100 100">
        <g>
          <ellipse cx="50" cy="16" rx="7" ry="14"/>
          <ellipse cx="50" cy="16" rx="7" ry="14" transform="rotate(30 50 50)"/>
          <ellipse cx="50" cy="16" rx="7" ry="14" transform="rotate(60 50 50)"/>
          <ellipse cx="50" cy="16" rx="7" ry="14" transform="rotate(90 50 50)"/>
          <ellipse cx="50" cy="16" rx="7" ry="14" transform="rotate(120 50 50)"/>
          <ellipse cx="50" cy="16" rx="7" ry="14" transform="rotate(150 50 50)"/>
          <ellipse cx="50" cy="16" rx="7" ry="14" transform="rotate(180 50 50)"/>
          <ellipse cx="50" cy="16" rx="7" ry="14" transform="rotate(210 50 50)"/>
          <ellipse cx="50" cy="16" rx="7" ry="14" transform="rotate(240 50 50)"/>
          <ellipse cx="50" cy="16" rx="7" ry="14" transform="rotate(270 50 50)"/>
          <ellipse cx="50" cy="16" rx="7" ry="14" transform="rotate(300 50 50)"/>
          <ellipse cx="50" cy="16" rx="7" ry="14" transform="rotate(330 50 50)"/>
        </g>
        <circle class="cut" cx="50" cy="50" r="18"/>
        <circle cx="50" cy="50" r="13"/>
      </svg>
    </li>
    <!-- flower -->
    <li class="menu-tile" aria-label="フラワー">
      <svg class="menu-icon" viewBox="0 0 100 100">
        <circle cx="50" cy="26" r="20"/>
        <circle cx="73" cy="43" r="20"/>
        <circle cx="64" cy="71" r="20"/>
        <circle cx="36" cy="71" r="20"/>
        <circle cx="27" cy="43" r="20"/>
        <circle cx="50" cy="50" r="20"/>
        <circle class="cut" cx="50" cy="50" r="7"/>
      </svg>
    </li>
    <!-- car -->
    <li class="menu-tile" aria-label="ドライブ">
      <svg class="menu-icon" viewBox="0 0 100 100">
        <path d="M6 66c0-10 6-16 16-18l12-14h26l14 14c12 2 20 6 20 18z"/>
        <path class="cut" d="M38 38h10v10H30zM52 38h8l10 10H52z"/>
        <circle cx="26" cy="70" r="13"/>
        <circle cx="74" cy="70" r="13"/>
        <circle class="cut" cx="26" cy="70" r="5"/>
        <circle class="cut" cx="74" cy="70" r="5"/>
      </svg>
    </li>
    <!-- drink -->
    <li class="menu-tile" aria-label="カフェ">
      <svg class="menu-icon" viewBox="0 0 100 100">
        <path d="M28 36h44l-6 56H34z"/>
        <path class="line" d="M54 36L58 16l16-8"/>
      </svg>
    </li>
    <!-- house -->
    <li class="menu-tile" aria-label="住まい">
      <svg class="menu-icon" viewBox="0 0 100 100">
        <path d="M50 10l40 34H80v44H20V44H10z"/>
        <rect class="cut" x="30" y="52" width="14" height="14"/>
        <rect class="cut" x="54" y="60" width="14" height="28"/>
        <path d="M80 88h10v-8h-10zM84 80h6v-8h-6z"/>
      </svg>
    </li>
  </ul>
</main>
</body>
</html>
```